Nu Upsilon civil engineering orgnization activities flyer

we need flyer design for Nu Upsilon civil engineering honor society in University of Brenmoor for science and technology. the flyer contain the schedule of the expected activity. the design should have a purple color and Nu Upsilon Key and logo (you will find them in the attached file) and the design should have something referring to civil engineering

Industry/Entity Type

Education

Colors
6b449b

Requirements
Must have
• Nu Upsilon logo, key, motto
Nice to have
• civil engineering samples, purple color

```html
<!DOCTYPE html>
<html lang="en">
<head>
<meta charset="utf-8">
<title>Nu Upsilon – Activities Flyer</title>
<link href="https://fonts.googleapis.com/css2?family=Jost:wght@500;600;700&family=Lato:wght@400;700&display=swap" rel="stylesheet">
<style>
  :root {
    --purple: #6b449b;
    --purple-deep: #4e2a7f;
    --purple-light: #8a5fc0;
    --purple-band: rgba(78, 42, 127, 0.88);
    --ink: #1f1a24;
    --paper: #ffffff;
    --backdrop: #dcdcdc;
    --sky-warm: #d9a98a;
    --sky-haze: #9a85a8;
  }
  * { box-sizing: border-box; margin: 0; padding: 0; }
  html, body { width: 1200px; height: 840px; overflow: hidden; }
  body {
    background: var(--backdrop);
    font-family: "Lato", Arial, sans-serif;
    color: var(--ink);
  }
  .flyer {
    position: absolute;
    left: 320px; top: 40px;
    width: 560px; height: 760px;
    background: var(--paper);
    box-shadow: 0 8px 24px rgba(0,0,0,0.18);
    overflow: hidden;
  }
  .section-title {
    font-family: "Jost", Arial, sans-serif;
    font-weight: 700;
    color: var(--purple);
    font-size: 15px;
    letter-spacing: 0.5px;
  }
  .meeting { position: absolute; left: 28px; top: 24px; right: 28px; }
  .schedule {
    margin-top: 8px;
    width: 100%;
    border-collapse: collapse;
    font-size: 10.5px;
    color: #fff;
  }
  .schedule th {
    background: var(--purple-light);
    font-family: "Jost", Arial, sans-serif;
    font-weight: 500;
    padding: 5px 6px;
    text-align: center;
  }
  .schedule td {
    background: var(--purple);
    padding: 4px 6px;
    text-align: center;
    border-bottom: 1px solid rgba(255,255,255,0.35);
    line-height: 1.25;
  }
  .scene {
    position: absolute;
    left: 0; right: 0; top: 262px; height: 420px;
    background:
      linear-gradient(to bottom, rgba(255,255,255,0) 70%, #fff 100%),
      linear-gradient(160deg, var(--sky-haze) 0%, var(--sky-warm) 40%, #7b5a8e 75%, #3f2a55 100%);
  }
  .activities { position: absolute; left: 0; top: 262px; width: 330px; }
  .band {
    background: var(--purple-band);
    color: #fff;
    font-family: "Jost", Arial, sans-serif;
    font-weight: 700;
    font-size: 15px;
    letter-spacing: 0.5px;
    padding: 3px 28px;
    width: 150px;
  }
  .details {
    padding: 6px 28px 10px;
    font-size: 10px;
    line-height: 1.35;
    color: #fff;
    text-shadow: 0 1px 2px rgba(0,0,0,0.35);
  }
  .details strong { font-weight: 700; }
  .service-details { color: var(--ink); text-shadow: none; }
  .brand {
    position: absolute; left: 48px; top: 650px;
    display: flex; align-items: center; gap: 10px;
  }
  .brand-mark { width: 18px; height: 18px; background: var(--purple); }
  .brand-name {
    font-family: "Jost", Arial, sans-serif;
    font-weight: 700;
    font-size: 30px;
    color: var(--purple);
  }
</style>
</head>
<body>
  <main class="flyer">
    <section class="meeting">
      <h2 class="section-title">Meeting</h2>
      <table class="schedule">
        <thead>
          <tr><th>Meeting No.</th><th>Date</th><th>Time</th><th>Location</th><th>Name</th><th>Company</th></tr>
        </thead>
        <tbody>
          <tr><td>1</td><td>9/8/2015</td><td>7 PM</td><td>BCH 124</td><td>Dr. Halvorsen</td><td>Brenmoor Waterworks</td></tr>
          <tr><td>2</td><td>9/22/2015</td><td>7 PM</td><td>BCH 124</td><td>Dane Whitcomb</td><td>Fort Kestrel</td></tr>
          <tr><td>3</td><td>10/6/2015</td><td>7 PM</td><td>BCH 124</td><td>Perry Ashdown</td><td>Tarvo Inc.</td></tr>
          <tr><td>4</td><td>10/20/2015</td><td>7 PM</td><td>BCH 124</td><td>Casey Mirefield</td><td>Linwell Partners</td></tr>
          <tr><td>5</td><td>11/3/2015</td><td>7 PM</td><td>BCH 124</td><td>Scavenger Hunt</td><td>Social</td></tr>
          <tr><td>6</td><td>11/17/2015</td><td>7 PM</td><td>BCH 124</td><td>Nomination/<br>Owen Strand</td><td></td></tr>
          <tr><td>7</td><td>12/1/2015</td><td>7 PM</td><td>BCH 124</td><td>Elections</td><td></td></tr>
        </tbody>
      </table>
    </section>

    <div class="scene" role="img" aria-label="Civil engineer in a purple hard hat and high-visibility jacket holding a survey instrument, with a historic city skyline at sunset behind him"></div>

    <section class="activities">
      <h2 class="band">Service</h2>
      <div class="details service-details">
        <p><strong>Alder Creek Conservation Area Service Day /</strong><br>Saturday, Oct 24, 11 am /<br>Alder Creek Conservation Area, Brenmoor, MO 65900, United States</p>
        <p><strong>Community Partnership Service Day /</strong><br>Saturday, Nov 7, 11 am / The Neighborhood Alliance<br>Resale Shop, 2200 N Harlow Ave, Brenmoor, MO 65900, United States</p>
        <p><strong>Tri Valley Animal Shelter Volunteer Day /</strong> Thursday, Nov 12, 12 pm /<br>Tri Valley Animal Shelter, 610 E Maple St, Ashford,<br>MO 65950, United States</p>
      </div>
      <h2 class="band">Social</h2>
      <div class="details">
        <p>Nu Upsilon Smoker<br>Bowling / Starlite Lanes (1040 Queens Parkway) /<br>Wednesday, October 28th / 9:00 PM<br>Plaque Signing / When: December 8th / the Hub</p>
      </div>
      <h2 class="band">Initiation</h2>
      <div class="details">
        <p>6:30PM initiation diner / Marlowe's - 1200 &nbsp;12/12/2015 &nbsp;5 PM-6PM &nbsp;BCH 314<br>North Oak Street, Ashford,</p>
      </div>
    </section>

    <div class="brand">
      <span class="brand-mark"></span>
      <span class="brand-name">Nu Upsilon</span>
    </div>
  </main>
</body>
</html>
```